Business Card Design Project - IT Company

CLOUD IT company working with medium to large corporate clients requires 2 sided Business Card design.

Strong, Professional and modern is what I am looking for.

The Logo JPG attached has all the colour palette options. which consist of Red and Silver on various backgrounds

Preferred option for the Back of card is either Silver Text on Red or Silver Text on Black. Though this is not concrete. Surprise me.

Logo must be prominent along with Contact details of the staff member

Tagline can be all Capitals " CLOUD MANAGED SERVICES"

I will look to provide feedback and tweaks to get the right design so it should be a fun process.

I will provide the layered files to the top few contenders.

Reason: Leaving the door open for some creativity. Don't forget this is an technology company. .

Target Market(s)

Leaders, decision makers, CEOs, CIOs,

Industry/Entity Type

Business

Requirements
Must have
• Data must have is

Company Name: Velquora
Tagline: Cloud Managed Services

No Particular order

First Name Last name
Director
Mobile 0452 987 654
www.velquora.com
First.Lastname@velquora.com
Suite 5, 48 Marlowe Lane, Sydney NSW 2000

```html
<!DOCTYPE html>
<html lang="en">
<head>
<meta charset="utf-8">
<title>Velquora Business Card</title>
<link href="https://fonts.googleapis.com/css2?family=Arimo:wght@400;700&display=swap" rel="stylesheet">
<style>
  :root {
    --backdrop: #e9e6e3;
    --card-white: #ffffff;
    --card-black: #030303;
    --brand-red: #9e2a2b;
    --ink-dark: #2e2e30;
    --ink-black: #111111;
    --silver: #dcdcdc;
    --silver-soft: #c9c9c9;
  }
  * { box-sizing: border-box; margin: 0; padding: 0; }
  html, body { width: 1200px; height: 1000px; overflow: hidden; }
  body {
    background: var(--backdrop);
    font-family: "Arimo", Arial, sans-serif;
    position: relative;
  }
  .card {
    position: absolute;
    left: 304px;
    width: 592px;
    height: 320px;
    border-radius: 18px;
    overflow: hidden;
  }
  .card-front { top: 178px; background: var(--card-white); }
  .card-back { top: 516px; background: var(--card-black); }

  /* Front */
  .front-brand {
    position: absolute;
    left: 40px;
    top: 100px;
    display: flex;
    align-items: center;
    gap: 18px;
  }
  .brand-dot {
    width: 74px; height: 74px; border-radius: 50%;
    background: var(--brand-red);
    flex: none;
  }
  .brand-words { display: flex; flex-direction: column; }
  .brand-name {
    font-weight: 700;
    font-size: 84px;
    line-height: 78px;
    color: var(--ink-dark);
    letter-spacing: -1px;
  }
  .brand-tagline {
    font-size: 18px;
    font-weight: 700;
    color: var(--ink-dark);
    letter-spacing: 0.5px;
    margin-left: 4px;
  }
  .front-person {
    position: absolute;
    right: 56px;
    top: 259px;
    text-align: right;
  }
  .front-person .person-name {
    font-size: 16px; font-weight: 700; color: var(--ink-black);
  }
  .front-person .person-role {
    margin-top: 5px;
    display: flex; justify-content: center; align-items: center; gap: 5px;
    font-size: 11px; font-weight: 700; color: var(--brand-red); letter-spacing: 0.5px;
  }
  .role-dot { width: 12px; height: 12px; border-radius: 50%; background: currentColor; }

  /* Back */
  .gloss { position: absolute; inset: 0; }
  .back-person {
    position: absolute; left: 0; right: 0; top: 46px;
    text-align: center; color: var(--silver);
  }
  .back-person .person-name { font-size: 36px; font-weight: 700; }
  .back-person .person-role {
    margin-top: 10px;
    display: flex; justify-content: center; align-items: center; gap: 7px;
    font-size: 18px; font-weight: 700;
  }
  .back-person .role-dot { width: 22px; height: 22px; }
  .back-person .address { margin-top: 20px; font-size: 13px; font-weight: 700; }

  .contact-tab {
    position: absolute; left: 0; top: 210px;
    width: 36px; height: 78px;
    background: var(--brand-red);
    border-radius: 0 4px 4px 0;
    display: flex; flex-direction: column; justify-content: space-around; align-items: center;
    padding: 3px 0;
  }
  .contact-tab svg { width: 16px; height: 16px; }
  .contact-list {
    position: absolute; left: 55px; top: 214px;
    list-style: none; color: var(--silver);
    font-size: 12.5px; font-weight: 700;
  }
  .contact-list li { height: 25px; }

  .back-brand {
    position: absolute; left: 274px; top: 222px;
    display: flex; align-items: center; gap: 10px;
  }
  .back-brand .brand-dot { width: 52px; height: 52px; background: var(--silver-soft); }
  .back-brand .brand-name { font-size: 52px; line-height: 50px; color: var(--silver-soft); }
  .back-brand .brand-tagline { font-size: 11px; color: var(--silver-soft); margin-left: 3px; }
</style>
</head>
<body>

<section class="card card-front">
  <div class="front-brand">
    <span class="brand-dot"></span>
    <div class="brand-words">
      <span class="brand-name">Velquora</span>
      <span class="brand-tagline">CLOUD MANAGED SERVICES</span>
    </div>
  </div>
  <div class="front-person">
    <p class="person-name">First Name Last name</p>
    <p class="person-role"><span class="role-dot"></span>DIRECTOR</p>
  </div>
</section>

<section class="card card-back">
  <svg class="gloss" width="592" height="320" viewBox="0 0 592 320" aria-hidden="true">
    <defs>
      <linearGradient id="glossFill" x1="0" y1="0" x2="1" y2="0.3">
        <stop offset="0" stop-color="#ffffff" stop-opacity="0.28"/>
        <stop offset="0.6" stop-color="#ffffff" stop-opacity="0.08"/>
        <stop offset="1" stop-color="#ffffff" stop-opacity="0"/>
      </linearGradient>
    </defs>
    <polygon points="446,0 592,0 592,320 330,320" fill="url(#glossFill)"/>
  </svg>

  <div class="back-person">
    <p class="person-name">First Name Last name</p>
    <p class="person-role"><span class="role-dot"></span>DIRECTOR</p>
    <p class="address">Suite 5, 48 Marlowe Lane, Sydney NSW 2000</p>
  </div>

  <div class="contact-tab">
    <svg viewBox="0 0 16 16" fill="none" stroke="#fff" stroke-width="1.2" aria-label="Email">
      <rect x="1.5" y="3.5" width="13" height="9"/><path d="M1.5 3.5 8 9l6.5-5.5"/>
    </svg>
    <svg viewBox="0 0 16 16" fill="none" stroke="#fff" stroke-width="1.2" aria-label="Website">
      <circle cx="8" cy="8" r="6.5"/><ellipse cx="8" cy="8" rx="3" ry="6.5"/><path d="M1.5 8h13M2.5 4.8h11M2.5 11.2h11"/>
    </svg>
    <svg viewBox="0 0 16 16" fill="none" stroke="#fff" stroke-width="1.2" aria-label="Phone">
      <path d="M4 1.8 6 5 4.8 6.4c.8 1.8 2.4 3.5 4.4 4.6L10.6 9.8l3.2 2-1.2 2.4C8 14 2.2 8.6 1.8 3.2Z"/>
    </svg>
  </div>
  <ul class="contact-list">
    <li>First.Lastname@velquora.com</li>
    <li>www.velquora.com</li>
    <li>0452 987 654</li>
  </ul>

  <div class="back-brand">
    <span class="brand-dot"></span>
    <div class="brand-words">
      <span class="brand-name">Velquora</span>
      <span class="brand-tagline">CLOUD MANAGED SERVICES</span>
    </div>
  </div>
</section>

</body>
</html>
```